Fundraising Study Day East of England. Lift the January blues!

A flyer to advertise a fundraising event of lectures for dental hygienists and therapists in support of the exemption campaign. Currently dental hygienists and therapists require a prescription to deliver certain treatment or recommend certain toothpastes. If we are successful in the campaign we will be able to treat patients without these restrictions.

Industry/Entity Type

Dental

```html
<!DOCTYPE html>
<html lang="en">
<head>
<meta charset="utf-8">
<title>Fundraising Study Day East of England</title>
<link rel="stylesheet" href="https://fonts.googleapis.com/css2?family=Raleway:wght@300;400;500;600;700;800&family=Titan+One&display=swap">
<style>
:root{
  --blue:#2c5b93;
  --grey-band:#f1f2f4;
  --row:#e4e5e7;
  --row-light:#eeeff0;
  --ink:#222;
  --red:#d42a22;
  --white:#fff;
  --backdrop:#e9e6e1;
}
*{margin:0;padding:0;box-sizing:border-box}
html,body{width:1200px;height:864px;overflow:hidden;background:var(--backdrop);font-family:"Raleway",sans-serif}
.canvas{position:relative;width:1200px;height:864px}
.page{position:absolute;top:56px;width:663px;height:938px;background:var(--white);transform:scale(.8);transform-origin:0 0;overflow:hidden;box-shadow:0 3px 10px rgba(0,0,0,.18)}
.page--info{left:53px}
.page--cover{left:619px}
.page-bg{position:absolute;inset:0;width:663px;height:938px}

/* info page */
.tab-title{position:absolute;left:50px;top:72px;font-size:26px;font-weight:800;color:var(--blue);letter-spacing:-.3px}
.description{position:absolute;left:68px;top:126px;width:528px;color:var(--white);font-size:15px;line-height:16px;text-align:justify;font-weight:400}
.detail{position:absolute;left:24px;width:340px;text-align:center;color:var(--ink)}
.detail-label{display:flex;align-items:center;justify-content:center;gap:10px;color:var(--blue);font-weight:600;font-size:14px;margin-bottom:10px;height:18px}
.detail-text{font-size:14px;white-space:nowrap}
.detail--location{top:303px}
.detail--date{top:377px}
.price-tag{position:absolute;left:376px;top:343px;width:194px;height:94px;background:var(--red);border-radius:6px;transform:rotate(-8deg);display:flex;flex-direction:column;align-items:center;justify-content:center;color:var(--white);font-family:"Titan One",sans-serif;line-height:1}
.price-tag .word{font-size:38px}
.price-tag .amount{font-size:37px;margin-top:2px}
.agenda{position:absolute;left:68px;top:513px;width:528px}
.agenda-title{height:45px;background:var(--blue);color:var(--white);font-size:24px;font-weight:700;text-align:center;line-height:45px}
.agenda-row{display:flex;margin-top:5px}
.agenda-time{width:78px;background:var(--row-light);font-size:9.5px;text-align:center;padding-top:10px;line-height:13px}
.agenda-time .gap{display:block;height:12px}
.agenda-time em{font-style:italic;font-weight:600}
.agenda-body{flex:1;background:var(--row);font-size:9.5px;line-height:12px;padding:10px 12px}
.agenda-body b{font-weight:700}
.agenda-body p + p{margin-top:4px}
.footer-url{position:absolute;left:0;width:663px;top:908px;text-align:center;color:var(--white);font-size:9.5px}

/* cover page */
.logo-spot{position:absolute;left:277px;top:36px;width:108px;height:108px;border-radius:50%;background:var(--blue);color:var(--white);display:flex;align-items:center;justify-content:center;text-align:center;font-size:13px;font-weight:600;line-height:16px}
.headline{position:absolute;left:0;top:166px;width:663px;text-align:center;color:var(--blue);font-size:40px;line-height:47px;font-weight:400;letter-spacing:-.3px}
.headline strong{font-weight:800}
.photo-area{position:absolute;inset:0}
.site-url{position:absolute;left:0;top:860px;width:663px;text-align:center;color:var(--white);font-size:22px;letter-spacing:2px;font-weight:400}
</style>
</head>
<body>
<div class="canvas">

  <section class="page page--info">
    <svg class="page-bg" viewBox="0 0 663 938" aria-hidden="true">
      <polygon points="0,0 663,0 663,238 0,270" fill="var(--blue)"/>
      <polygon points="0,270 663,238 663,485 0,460" fill="var(--grey-band)"/>
      <polygon points="0,66 105,66 110,62 240,66 273,108 0,108" fill="var(--white)"/>
      <polygon points="0,938 48,898 595,882 663,938" fill="var(--blue)"/>
    </svg>

    <h2 class="tab-title">DESCRIPTION</h2>
    <p class="description">A fundraising event to support our exemptions project. The day will consist of a series of presentations ranging from the new ECPD to new technologies. The aim, being to enhance our learning and raise funds to support the exemptions campaign. The speaker line includes some of the UK and Irelands most respected dental professionals in our field.</p>

    <div class="detail detail--location">
      <div class="detail-label">
        <svg width="16" height="20" viewBox="0 0 16 20" aria-hidden="true"><path d="M8 1a6 6 0 0 0-6 6c0 4.5 6 11 6 11s6-6.5 6-11a6 6 0 0 0-6-6z" fill="none" stroke="var(--blue)" stroke-width="2"/><circle cx="8" cy="7" r="2.2" fill="var(--blue)"/></svg>
        LOCATION
      </div>
      <div class="detail-text">Harrow Hotel, Mead Way, Ashby, AB12 3CD</div>
    </div>

    <div class="detail detail--date">
      <div class="detail-label">
        <svg width="20" height="18" viewBox="0 0 20 18" aria-hidden="true"><rect x="1" y="3" width="15" height="13" fill="none" stroke="var(--blue)" stroke-width="1.6"/><path d="M1 7h15M5 1v4M12 1v4" stroke="var(--blue)" stroke-width="1.6"/><circle cx="15" cy="13" r="4" fill="var(--white)" stroke="var(--blue)" stroke-width="1.4"/><path d="M15 11v2h1.5" stroke="var(--blue)" stroke-width="1.2" fill="none"/></svg>
        DATE AND TIME
      </div>
      <div class="detail-text">Fri 19 January 2018 | 09:00 – 16:30 GMT</div>
    </div>

    <div class="price-tag"><span class="word">COST</span><span class="amount">£101.48</span></div>

    <div class="agenda">
      <div class="agenda-title">AGENDA</div>
      <div class="agenda-row" style="height:33px">
        <div class="agenda-time">9.30 - 10.15</div>
        <div class="agenda-body"><b>Fiona Marsh:</b> Immediate past president of the HTS will be updating us on all things</div>
      </div>
      <div class="agenda-row" style="height:71px">
        <div class="agenda-time">10.15 - 11.00<span class="gap"></span>11.00 - 11.30<br><em>BREAK</em></div>
        <div class="agenda-body"><p><b>Megan Holloway:</b> Will provide an update on teeth whitening and explain how social media has impacted her business</p><p><b>Julia Renwick:</b> Our internationally acclaimed speaker will update our knowledge of periodontal disease and nutrition and new technologies.</p></div>
      </div>
      <div class="agenda-row" style="height:70px">
        <div class="agenda-time">11.30 - 13.00<span class="gap"></span>13.00 - 14.00<br><em>LUNCH</em></div>
        <div class="agenda-body">Sinead Carver &amp; Melanie Pryor: Will be providing a combined presentation on ‘Scaling your business’ and start to finish Sonicflow techniques. The aim being to build our business with effective communications, systems and protocols. This sessions promises audience participation!</div>
      </div>
      <div class="agenda-row" style="height:47px">
        <div class="agenda-time">14.00 - 15.00<br>15.00 - 15.30<br>BREAK</div>
        <div class="agenda-body"><b>Paul Pender:</b> Save your back. All things posture</div>
      </div>
      <div class="agenda-row" style="height:44px">
        <div class="agenda-time">15.30 16.30</div>
        <div class="agenda-body"><b>Julia Renwick:</b> Our internationally acclaimed speaker will update our knowledge of periodontal disease and nutrition and new technologies.</div>
      </div>
    </div>

    <div class="footer-url">https://www.ticketfield.co.uk/e/fundraising-study-day-east-of-england-lift-the-january-blues-tickets-10293847</div>
  </section>

  <section class="page page--cover">
    <svg class="photo-area" viewBox="0 0 663 938" role="img" aria-label="Photo of a smiling patient in a dental chair with a dentist holding a mirror and probe">
      <defs>
        <linearGradient id="photoTone" x1="0" y1="0" x2="1" y2="1">
          <stop offset="0" stop-color="#e9ddd6"/>
          <stop offset=".45" stop-color="#c9b2a8"/>
          <stop offset=".75" stop-color="#8fc3cf"/>
          <stop offset="1" stop-color="#dfe6ea"/>
        </linearGradient>
      </defs>
      <polygon points="0,382 663,330 663,850 0,720" fill="url(#photoTone)"/>
      <polygon points="0,720 663,850 663,938 0,938" fill="var(--blue)"/>
    </svg>

    <div class="logo-spot">LOGO<br>WILL<br>COME<br>HERE</div>
    <h1 class="headline"><strong>FUNDRAISING</strong> STUDY DAY<br>EAST OF ENGLAND.<br><strong>LIFT THE JANUARY BLUES!</strong></h1>
    <div class="site-url">www.studydayevents.com</div>
  </section>

</div>
</body>
</html>
```